Selvin: A Friday night in the Prophetic Flyer

We are holding 2 Friday night events, one on 10/25/19 and the other on 11/29/19.
The time frame is 6:30pm-9:00pm. These services will be a time of prayer/healing for the sick and will be prophetic as well. (There will be prophets prophesying over people)

The event is called: Selvin: A Friday night in the Prophetic
The flyer should also include the phrase/excerpt: "And they prophesied also".

Keywords/Phrases: Prophetic, Healing, Climbing in the Spirit, Higher level of Anointing...

Target Market(s)

those looking for healing, seeking a word from God

Colors

Designer to choose colors to be used in the design.

Requirements
Must have
• The event is called: Selvin: A Friday night in the Prophetic
• The flyer should also include the phrase/excerpt: "And they prophesied also".
• It must include the Tovik logo attached, either is fine, we have attached two different versions.
• It must have the dates, location, time
• Dates: October 25, 2019 and November 29, 2019
• Location: Hollard Community Center
• (Downtown Portland) 482 Wendle Street
• Portland, ME 04102
• Time: 6:30pm-9:00pm
• Contact Info: Tel. 207-555-3841
• email: contact@brimfield-hall.org
• web: www.tovik.org
Nice to have
• creativity in color scheme, the meaning of the word Selvin conveyed in a classy artistic way/design.
Should not have
• Crosses, pictures of churches

```html
<!DOCTYPE html>
<html lang="en">
<head>
<meta charset="utf-8">
<title>Selvin: A Friday night in the Prophetic</title>
<link rel="stylesheet" href="https://fonts.googleapis.com/css2?family=Dancing+Script:wght@700&family=Roboto+Condensed:wght@400;700&display=swap">
<style>
  :root {
    --navy: #04375b;
    --orange: #f7941d;
    --white: #ffffff;
    --page: #ffffff;
    --photo-warm: #b8502a;
    --photo-mid: #8a5a4a;
    --photo-cool: #c9c4c2;
  }
  * { margin: 0; padding: 0; box-sizing: border-box; }
  html, body { width: 966px; height: 1200px; overflow: hidden; background: var(--page); }
  .canvas { position: relative; width: 966px; height: 1200px; background: var(--page); }
  .flyer {
    position: absolute; left: 78px; top: 68px; width: 815px; height: 1057px;
    background: var(--navy); overflow: hidden;
    font-family: "Roboto Condensed", "Arial Narrow", sans-serif;
  }
  .hero-art { position: absolute; left: 0; top: 0; width: 815px; height: 960px; }
  .brand {
    position: absolute; left: 585px; top: 96px;
    display: flex; align-items: center; gap: 10px;
    color: var(--white); font-weight: 700; font-size: 40px; letter-spacing: 1px;
  }
  .brand-dot { width: 16px; height: 16px; border-radius: 50%; background: var(--orange); }
  .event-title {
    position: absolute; left: 95px; top: 88px;
    font-family: "Dancing Script", cursive; font-weight: 700;
    font-size: 158px; line-height: 1; color: var(--orange);
    text-shadow: 3px 3px 0 var(--white);
    white-space: nowrap;
  }
  .event-subtitle {
    position: absolute; left: 257px; top: 236px; width: 419px; height: 50px;
    background: var(--orange); border-radius: 3px;
    color: var(--navy); font-weight: 700; font-size: 31px;
    display: flex; align-items: center; justify-content: center;
    white-space: nowrap;
  }
  .scripture {
    position: absolute; right: 143px; top: 300px;
    color: var(--white); font-weight: 700; font-size: 21px;
  }
  .dates {
    position: absolute; left: 122px; top: 378px;
    color: var(--white); font-weight: 700; font-size: 34px;
    white-space: nowrap;
  }
  .venue { position: absolute; left: 122px; top: 448px; }
  .venue-name { color: var(--orange); font-weight: 700; font-size: 42px; line-height: 1.1; white-space: nowrap; }
  .venue-address { color: var(--white); font-weight: 700; font-size: 25px; line-height: 34px; margin-top: 2px; }
  .event-time { color: var(--orange); font-weight: 700; font-size: 25px; line-height: 34px; margin-top: 4px; }
  .contact-bar {
    position: absolute; left: 0; bottom: 0; width: 815px; height: 97px;
    background: var(--orange);
    display: flex; align-items: center; justify-content: center;
    color: var(--navy); font-weight: 700; font-size: 29px;
    white-space: nowrap;
  }
  .contact-item { padding: 0 18px; }
  .contact-divider { width: 2px; height: 52px; background: var(--white); }
</style>
</head>
<body>
<div class="canvas">
  <main class="flyer">
    <svg class="hero-art" viewBox="0 0 815 960">
      <defs>
        <linearGradient id="worship-tones" x1="0" y1="1" x2="1" y2="0">
          <stop offset="0" stop-color="#b8502a"/>
          <stop offset="0.5" stop-color="#8a5a4a"/>
          <stop offset="1" stop-color="#c9c4c2"/>
        </linearGradient>
      </defs>
      <polygon class="accent-stripe" points="0,780 815,499 0,822" fill="#f7941d"/>
      <polygon class="worship-photo" role="img" aria-label="Photo of a worship crowd with raised hands in warm stage light" points="0,822 815,499 815,960 0,960" fill="url(#worship-tones)"/>
    </svg>

    <div class="brand"><span class="brand-dot"></span><span class="brand-name">TOVIK</span></div>

    <h1 class="event-title">Selvin</h1>
    <div class="event-subtitle">A Friday night in the Prophetic</div>
    <p class="scripture">“And they prophesied also”</p>

    <p class="dates">October 25, 2019 and November 29, 2019</p>

    <div class="venue">
      <p class="venue-name">Hollard Community Center</p>
      <p class="venue-address">(Downtown Portland) 482 Wendle Street<br>Portland, ME 04102</p>
      <p class="event-time">6:30pm – 9:00pm</p>
    </div>

    <footer class="contact-bar">
      <span class="contact-item">207-555-3841</span>
      <span class="contact-divider"></span>
      <span class="contact-item">contact@brimfield-hall.org</span>
      <span class="contact-divider"></span>
      <span class="contact-item">www.tovik.org</span>
    </footer>
  </main>
</div>
</body>
</html>
```